New website for Pilates Studio

I need a new version of my website
http://brightcoreflow.biz/
I want an updated fresh look with an easier to read schedule that looks good on mobile phones as well as laptops.
Clean, simple, fresh and BOLD

Target Market(s)

All ages, genders and races

Coding

Number of Pages Required

Colors
9bcb3c

Requirements
Must have
• Photos that mostly use the real images from our studio. Browse our facebook page, website or ask me for high quality images

```html
<!DOCTYPE html>
<html lang="en">
<head>
<meta charset="utf-8">
<title>Bright Core Flow – Pilates &amp; Spiral Studio</title>
<link rel="stylesheet" href="https://fonts.googleapis.com/css2?family=Open+Sans:ital,wght@0,400;0,600;0,700;1,300;1,700&family=Oxygen:wght@300;400;700&family=Raleway:wght@400;500&display=swap">
<style>
:root{
  --green-dark:#4f7a22;
  --green-mid:#5d8a2a;
  --green-light:#86bb3c;
  --green-row:#7db236;
  --gold:#c9a02a;
  --ink:#333333;
  --muted:#666666;
  --panel:#f1f1f1;
  --footer:#262626;
  --footer-text:#bdbdbd;
  --white:#ffffff;
}
*{margin:0;padding:0;box-sizing:border-box}
html,body{width:835px;height:1200px;overflow:hidden;background:var(--white)}
body{position:relative;font-family:"Open Sans",sans-serif;color:var(--ink)}
.abs{position:absolute}

/* header */
.site-header{position:absolute;left:0;top:0;width:835px;height:60px;z-index:3}
.brand-plate{position:absolute;left:0;top:0;width:300px;height:60px;background:var(--white);clip-path:polygon(0 0,258px 0,300px 30px,258px 60px,0 60px)}
.brand-name{position:absolute;left:90px;top:18px;font-family:"Oxygen",sans-serif;font-weight:700;font-size:18px;color:var(--green-dark)}
.brand-dot{position:absolute;left:72px;top:20px;width:14px;height:14px;border-radius:50%;border:3px solid var(--gold)}
.main-nav{position:absolute;left:300px;top:9px;width:535px;height:41px;background:linear-gradient(90deg,#6a9431,var(--green-dark));clip-path:polygon(0 0,100% 0,100% 100%,0 100%,20px 50%)}
.main-nav a{position:absolute;top:13px;font-size:10px;font-weight:600;color:var(--white);text-decoration:none}
.nav-marker{position:absolute;left:99px;top:6px;width:24px;height:24px;border:2px solid var(--white);border-radius:50%;border-right-color:transparent;border-top-color:transparent}

/* hero */
.hero{position:absolute;left:0;top:60px;width:835px;height:387px}
.hero-photo{position:absolute;inset:0;background:linear-gradient(100deg,#d9cfc0 0%,#efe9df 30%,#e8e1d6 55%,#f3efe8 80%,#ddd6ca 100%)}
.hero-mat{position:absolute;left:0;bottom:0;width:560px;height:10px;background:linear-gradient(90deg,#3e9fc4,#7fc6de)}
.hero-copy{position:absolute;left:494px;top:103px;width:270px}
.hero-kicker{font-style:italic;font-weight:300;font-size:26px;line-height:30px;color:#3a3a3a;letter-spacing:.5px}
.hero-title{font-style:italic;font-weight:700;font-size:27px;line-height:32px;color:#2e2e2e}
.hero-title span{color:var(--green-dark)}
.hero-sub{font-family:"Oxygen",sans-serif;font-size:14px;color:#333;text-align:right;width:243px;margin-top:2px}
.hero-text{font-family:"Oxygen",sans-serif;font-size:9.5px;line-height:15px;color:#333;margin-top:10px;width:250px}
.btn-features{position:absolute;left:621px;top:240px;width:120px;height:30px;background:var(--green-dark);color:var(--white);font-family:"Oxygen",sans-serif;font-size:12px;line-height:30px;text-align:center;box-shadow:0 2px 4px rgba(0,0,0,.25)}

/* welcome */
.welcome-title{left:90px;top:476px;font-family:"Oxygen",sans-serif;font-weight:300;font-size:22px;color:#333}
.welcome-title strong{color:var(--green-dark);font-weight:700}
.welcome-body{left:90px;top:510px;width:306px;font-family:"Raleway",sans-serif;font-size:8.3px;line-height:13.5px;color:var(--muted);text-align:justify}
.welcome-body p+p{margin-top:6px}
.video{left:459px;top:484px;width:286px;height:154px;background:linear-gradient(110deg,#3a2a1c,#6b5238 45%,#4a3826)}
.video-play{position:absolute;left:119px;top:53px;width:48px;height:48px;border:3px solid var(--white);border-radius:50%}
.video-play::after{content:"";position:absolute;left:18px;top:12px;border-left:15px solid var(--white);border-top:9px solid transparent;border-bottom:9px solid transparent}

/* classes */
.classes{left:0;top:673px;width:835px;height:335px;background:var(--panel)}
.section-title{left:0;top:700px;width:835px;text-align:center;font-family:"Oxygen",sans-serif;font-weight:300;font-size:20px;color:#333}
.section-title strong{color:var(--green-dark);font-weight:700}
.title-rule{left:295px;top:740px;width:245px;height:1px;background:#b8b8b8}
.instructor{position:absolute;left:90px;width:316px;height:60px}
.instructor-card{position:absolute;left:30px;top:0;width:286px;height:60px;background:var(--white)}
.instructor-photo{position:absolute;left:0;top:1px;width:58px;height:58px;border-radius:50%;border:4px solid var(--gold);background:linear-gradient(135deg,#c9b8a4,#8c7a68)}
.instructor-name{position:absolute;left:70px;top:10px;font-size:10px;font-weight:600;color:#222}
.instructor-bio{position:absolute;left:70px;top:24px;width:212px;font-size:8.3px;line-height:12.5px;color:var(--muted)}
.card-corner{position:absolute;right:0;bottom:0;width:0;height:0;border-left:15px solid transparent;border-bottom:15px solid var(--green-dark)}
.card-corner-plus{position:absolute;right:2px;bottom:0;font-size:9px;font-weight:700;color:var(--white);line-height:10px}
.more-link{font-size:8.5px;font-weight:600;color:var(--green-dark)}

.schedule{left:430px;top:769px;width:316px;height:191px;background:var(--green-light)}
.schedule-head{position:absolute;left:0;top:0;width:316px;height:49px;background:var(--green-dark)}
.schedule-day{position:absolute;left:11px;top:8px;font-family:"Oxygen",sans-serif;font-size:17px;color:var(--white)}
.schedule-note{position:absolute;left:11px;top:31px;font-size:8px;color:var(--white)}
.day-arrow{position:absolute;top:15px;width:17px;height:17px;border:1.5px solid var(--white);border-radius:50%}
.day-arrow.next{border-color:#9bcb3c}
.day-arrow::after{content:"";position:absolute;top:4px;border-top:3px solid transparent;border-bottom:3px solid transparent}
.day-arrow.prev::after{left:4px;border-right:4px solid var(--white)}
.day-arrow.next::after{left:6px;border-left:4px solid #9bcb3c}
.schedule-table{position:absolute;left:0;top:49px;width:316px;border-collapse:collapse}
.schedule-table tr{height:23.7px;border-bottom:1px solid rgba(255,255,255,.25);background:linear-gradient(90deg,var(--green-row),#8cc243)}
.schedule-table th{text-align:left;padding-left:11px;width:103px;font-size:9.5px;font-weight:600;color:var(--white)}
.schedule-table td{width:35.5px;text-align:center;font-size:8px;color:var(--white)}

/* footer */
.site-footer{left:0;top:1008px;width:835px;height:192px;background:var(--footer)}
.badges{left:90px;top:1039px;width:150px;height:61px;background:var(--white)}
.badge{position:absolute;top:8px;width:44px;height:45px}
.badge-green{left:20px;border-radius:50%;background:#3f8d7e}
.badge-cert{left:82px;border-radius:4px;background:#cfd9e8;border:2px solid #2e5c8e}
.eco-note{left:90px;top:1111px;width:180px;font-size:7.8px;line-height:12px;color:var(--footer-text)}
.footer-heading{font-size:11px;font-weight:600;color:var(--white)}
.quick-links{left:299px;top:1064px;list-style:none}
.quick-links li{font-size:8.5px;line-height:19.2px;color:var(--footer-text)}
.quick-links li::before{content:"›";margin-right:6px;color:#ddd}
.contact-item{position:absolute;left:393px;display:flex;align-items:flex-start;gap:10px;font-size:8.3px;line-height:12px;color:var(--footer-text)}
.contact-icon{flex:none;width:20px;height:20px;border:1.5px solid #cfcfcf;border-radius:50%;display:flex;align-items:center;justify-content:center}
.footer-brand{left:567px;top:1047px;width:178px;text-align:right;font-family:"Oxygen",sans-serif;font-weight:700;font-size:20px;color:#a8a8a8}
.footer-brand-dot{left:567px;top:1049px;width:22px;height:22px;border:3px solid #a8a8a8;border-radius:50%}
.social{position:absolute;top:1105px;width:16px;height:16px;background:var(--white)}
.social.primary{background:#5a9e2f}
.copyright{left:567px;top:1143px;width:180px;text-align:center;font-size:7.6px;color:#cfcfcf}
</style>
</head>
<body>

<header class="site-header">
  <div class="brand-plate">
    <span class="brand-dot"></span>
    <span class="brand-name">Bright Core Flow</span>
  </div>
  <nav class="main-nav">
    <span class="nav-marker"></span>
    <a style="left:109px">Home</a>
    <a style="left:173px">Schedule</a>
    <a style="left:249px">Rates</a>
    <a style="left:310px">Instructors</a>
    <a style="left:394px">Contact Us</a>
  </nav>
</header>

<section class="hero">
  <div class="hero-photo" role="img" aria-label="Photo of a woman holding a pilates stretch on a mat in a bright studio"></div>
  <div class="hero-mat"></div>
  <div class="hero-copy">
    <div class="hero-kicker">PILATES &amp;</div>
    <div class="hero-title"><span>SPIRAL</span> STUDIO</div>
    <div class="hero-sub">State-of-the-art Facilities....</div>
    <p class="hero-text">Lorem ipsum dolor sit amet, consectetuer adipiscing elit, diam nonummy nibh euismod tincidunt ut  doloresi.</p>
  </div>
  <a class="btn-features">See All Features</a>
</section>

<h1 class="abs welcome-title">Welcome To <strong>Bright Core Flow</strong></h1>
<div class="abs welcome-body">
  <p>Bright Core Flow Pilates and SPIRAL Studio, in the heart of Cedar Village, is a warm, inviting studio where students and teachers alike are supported and encouraged to discover and grow at an individual pace through the field of integrated movement.</p>
  <p>We offer one-on-one sessions, group reformer classes and mat classes. Our mission is to promote long-term emotional and physical health through joyful, integrated movement training and to inspire and nurture our clients to learn more deeply about themselves and connect with fellow students and the community.</p>
</div>
<div class="abs video" role="img" aria-label="Video still of an instructor leading a class in the studio">
  <span class="video-play"></span>
</div>

<section class="abs classes"></section>
<h2 class="abs section-title">Our <strong>Classes</strong></h2>
<div class="abs title-rule"></div>

<article class="instructor" style="top:769px">
  <div class="instructor-card">
    <div class="instructor-name">Marla Fenwick</div>
    <p class="instructor-bio">Is our newest apprentice. Marla enjoys being active in any many ways including Pilates, swimming, water polo, and...</p>
    <span class="card-corner"></span><span class="card-corner-plus">+</span>
  </div>
  <div class="instructor-photo" role="img" aria-label="Portrait photo of instructor Marla Fenwick"></div>
</article>
<article class="instructor" style="top:835px">
  <div class="instructor-card">
    <div class="instructor-name">Noa Levine</div>
    <p class="instructor-bio">Emigrated from Israel 14 years ago and graduated from the Lakeside Conservatory of Performing Arts.</p>
    <span class="card-corner"></span><span class="card-corner-plus">+</span>
  </div>
  <div class="instructor-photo" role="img" aria-label="Portrait photo of instructor Noa Levine"></div>
</article>
<article class="instructor" style="top:900px">
  <div class="instructor-card">
    <div class="instructor-name">Tessa Holloway</div>
    <p class="instructor-bio">Has been teaching Pilates since 2004, bringing her love for movement into all of her classes and private sessions.</p>
    <span class="card-corner"></span><span class="card-corner-plus">+</span>
  </div>
  <div class="instructor-photo" role="img" aria-label="Portrait photo of instructor Tessa Holloway"></div>
</article>
<a class="abs more-link" style="left:316px;top:966px">Meet Our Instructors »</a>

<section class="abs schedule">
  <div class="schedule-head">
    <div class="schedule-day">MONDAY</div>
    <div class="schedule-note">Consectetuer adipiscing elit</div>
    <span class="day-arrow prev" style="left:266px"></span>
    <span class="day-arrow next" style="left:290px"></span>
  </div>
  <table class="schedule-table">
    <tr><th>Bootcamp Plus</th><td>6 AM</td><td>-</td><td>-</td><td>-</td><td>-</td><td>-</td></tr>
    <tr><th>Group Reformer*</th><td>8 AM</td><td>12 PM</td><td>5 PM</td><td>6 PM</td><td>7 PM</td><td>-</td></tr>
    <tr><th>Slow Pilates Mat</th><td>11 AM</td><td>-</td><td>-</td><td>-</td><td>-</td><td>-</td></tr>
    <tr><th>Pilates Mat</th><td>4 PM</td><td>-</td><td>-</td><td>-</td><td>-</td><td>-</td></tr>
    <tr><th>SpiralK</th><td>-</td><td>-</td><td>-</td><td>-</td><td>-</td><td>-</td></tr>
    <tr><th>Yoga</th><td>-</td><td>-</td><td>-</td><td>-</td><td>-</td><td>-</td></tr>
  </table>
</section>
<a class="abs more-link" style="left:677px;top:966px">View Schedule »</a>

<footer class="abs site-footer"></footer>
<div class="abs badges">
  <span class="badge badge-green" role="img" aria-label="Green business program badge"></span>
  <span class="badge badge-cert" role="img" aria-label="Pilates certification badge"></span>
</div>
<p class="abs eco-note">Join our community in creating a sustainable future. We enjoy the benefits of protecting our environment with daily practice: recycling, using efficient lighting, conserving water use, and acting responsibly.</p>

<div class="abs footer-heading" style="left:301px;top:1033px">Quick Link</div>
<ul class="abs quick-links">
  <li>Home</li><li>Schedule</li><li>Rates</li><li>Instructors</li><li>Contact Us</li>
</ul>

<div class="abs footer-heading" style="left:393px;top:1033px">Contact Us</div>
<div class="contact-item" style="top:1058px">
  <span class="contact-icon"><svg width="9" height="11" viewBox="0 0 9 11"><path d="M4.5 0A4 4 0 0 0 .5 4c0 3 4 7 4 7s4-4 4-7a4 4 0 0 0-4-4zm0 5.5a1.5 1.5 0 1 1 0-3 1.5 1.5 0 0 1 0 3z" fill="#ddd"/></svg></span>
  <span>2140 Harbor Lane #12<br>Cedarton,CA 95410</span>
</div>
<div class="contact-item" style="top:1092px">
  <span class="contact-icon"><svg width="10" height="10" viewBox="0 0 10 10"><path d="M2 0l2 2.5-1.2 1.3a6 6 0 0 0 3.4 3.4L7.5 6 10 8 8.5 9.8C4 9.5.5 6 .2 1.5z" fill="#ddd"/></svg></span>
  <span style="margin-top:4px">Call Us Now: 555.214.0392</span>
</div>
<div class="contact-item" style="top:1121px">
  <span class="contact-icon"><svg width="10" height="8" viewBox="0 0 10 8"><rect width="10" height="8" rx="1" fill="#ddd"/><path d="M0 1l5 3.5L10 1" stroke="#262626" fill="none"/></svg></span>
  <span style="margin-top:4px">info@brightcoreflow.biz</span>
</div>

<div class="abs footer-brand-dot"></div>
<div class="abs footer-brand">Bright Core Flow</div>
<span class="social primary" style="left:621px"></span>
<span class="social" style="left:643px"></span>
<span class="social" style="left:664px"></span>
<span class="social" style="left:686px"></span>
<p class="abs copyright">Copyright © 2015 bright core flow.</p>

</body>
</html>
```